Business Cards For A cell Phone Company
Linden Cellular
Business Cards For A cell Phone Company - Retailers
Creative Brief
Simple
Tobias Krell
Operations Manager
2864 Belmore Ave Cincinnati OH 45219
tobias.krell@lindencellular-mail.com
www.lindencellular-mail.com
Concepts
Business Cards/Letterhead/ Envelopes/Notepads/Tshirt/labels for quiet tin crate
Business cards and company letter head for Orchard Noodle Court

```html
<!DOCTYPE html>
<html lang="en">
<head>
<meta charset="utf-8">
<title>Linden Cellular – Business Card</title>
<link href="https://fonts.googleapis.com/css2?family=Montserrat:wght@400;500;600&display=swap" rel="stylesheet">
<style>
  :root {
    --backdrop: #e6e4e1;
    --card-white: #ffffff;
    --brand-red: #c8141c;
    --brand-red-dark: #8e0a10;
    --brand-red-light: #e2262d;
    --silver: #c9c9cb;
    --silver-dark: #9c9ca0;
    --text-light: #ffffff;
    --text-soft: #f6d9da;
  }
  * { margin: 0; padding: 0; box-sizing: border-box; }
  html, body {
    width: 1200px; height: 901px; overflow: hidden;
    background: var(--backdrop);
    font-family: "Montserrat", Arial, sans-serif;
  }
  .canvas {
    position: relative; width: 1200px; height: 901px;
    display: flex; align-items: center; justify-content: center;
  }
  .business-card {
    position: relative; width: 900px; height: 520px;
    border-radius: 36px; overflow: hidden;
    background: var(--card-white);
    box-shadow: 0 18px 40px rgba(0,0,0,0.18);
  }
  .card-art { position: absolute; inset: 0; width: 100%; height: 100%; }
  .brand {
    position: absolute; left: 470px; top: 112px;
    display: flex; align-items: center; gap: 16px;
  }
  .brand-dot {
    width: 54px; height: 54px; border-radius: 50%;
    background: var(--brand-red);
  }
  .brand-name {
    font-size: 36px; font-weight: 600; color: var(--brand-red);
    letter-spacing: 1px; white-space: nowrap;
  }
  .contact-person {
    position: absolute; left: 58px; top: 330px; color: var(--text-light);
  }
  .person-name { font-size: 22px; font-weight: 500; letter-spacing: 1.5px; text-transform: uppercase; }
  .person-title { font-size: 15px; color: var(--text-soft); margin-top: 4px; }
  .address { margin-top: 26px; font-size: 15px; line-height: 1.6; color: var(--text-light); }
  .contact-lines {
    position: absolute; right: 54px; top: 372px;
    list-style: none; color: var(--text-light); font-size: 14px; text-align: right;
  }
  .contact-lines li {
    display: flex; justify-content: flex-end; align-items: center; gap: 10px;
    height: 24px; white-space: nowrap;
  }
  .contact-lines svg { width: 14px; height: 14px; flex: none; fill: none; stroke: var(--text-light); stroke-width: 1.8; }
</style>
</head>
<body>
<main class="canvas">
  <section class="business-card">
    <svg class="card-art" viewBox="0 0 900 520" preserveAspectRatio="none" aria-hidden="true">
      <defs>
        <linearGradient id="redBand" x1="0" y1="0" x2="1" y2="1">
          <stop offset="0" stop-color="var(--brand-red-dark)"/>
          <stop offset="0.45" stop-color="var(--brand-red-light)"/>
          <stop offset="1" stop-color="var(--brand-red-dark)"/>
        </linearGradient>
        <linearGradient id="silverBand" x1="0" y1="0" x2="1" y2="0">
          <stop offset="0" stop-color="var(--silver-dark)"/>
          <stop offset="0.5" stop-color="#eeeeef"/>
          <stop offset="1" stop-color="var(--silver-dark)"/>
        </linearGradient>
      </defs>
      <path d="M0 250 C 220 190, 440 300, 620 270 C 760 248, 840 215, 900 200 L900 520 L0 520 Z" fill="url(#silverBand)"/>
      <path d="M0 275 C 220 215, 440 330, 620 300 C 760 278, 840 250, 900 238 L900 520 L0 520 Z" fill="url(#redBand)"/>
    </svg>

    <div class="brand">
      <span class="brand-dot"></span>
      <span class="brand-name">Linden Cellular</span>
    </div>

    <div class="contact-person">
      <p class="person-name">Tobias Krell</p>
      <p class="person-title">Operations Manager</p>
      <p class="address">2864 Belmore Ave<br>Cincinnati OH 45219</p>
    </div>

    <ul class="contact-lines">
      <li>513 555 0142
        <svg viewBox="0 0 16 16"><path d="M3 2 L6 2 L7 5 L5 6.5 C6 9 7 10 9.5 11 L11 9 L14 10 L14 13 C8 14 2 8 3 2 Z"/></svg></li>
      <li>513 555 0187
        <svg viewBox="0 0 16 16"><rect x="4" y="1.5" width="8" height="13" rx="1.5"/><line x1="7" y1="12" x2="9" y2="12"/></svg></li>
      <li>513 555 0163
        <svg viewBox="0 0 16 16"><rect x="2" y="5" width="12" height="7" rx="1"/><rect x="4.5" y="2" width="7" height="3"/></svg></li>
      <li>tobias.krell@lindencellular-mail.com
        <svg viewBox="0 0 16 16"><rect x="1.5" y="3.5" width="13" height="9" rx="1"/><path d="M1.5 4 L8 9 L14.5 4"/></svg></li>
      <li>www.lindencellular-mail.com
        <svg viewBox="0 0 16 16"><circle cx="8" cy="8" r="6.5"/><path d="M1.5 8 H14.5 M8 1.5 C5 5 5 11 8 14.5 M8 1.5 C11 5 11 11 8 14.5"/></svg></li>
    </ul>
  </section>
</main>
</body>
</html>
```